Beef Tallow Balm Jar Label Design

We need new labels for our beef tallow balm jar labels. We started pretty plain and it's time for a redesign.
We have three sizes of jars (9 oz, 4 oz, and 2 oz straight sided amber jars) we use with 7 scents for each size. (Changes would be scent name, UPC bar code, and essential oil portion of ingredients. If the files are setup for us to change those three items to generate additional options, that would be fine.)
The attached example will atleast give you an example of what is on our current labels.
Thank you!
Updates
A note about the maximum label sizes for the jars:
8 oz Jar: Max label size: 9" x 2"
4 oz jar: Max label size: 7" x 1.6"
2 oz jar: Max label size: 6.5" x 1"
Thank you!
Look and feel
Each slider illustrates characteristics of the customer's brand and the style your logo design should communicate.

```html
<!DOCTYPE html>
<html lang="en">
<head>
<meta charset="utf-8">
<title>Grass Fed Beef Tallow Balm – Peppermint Label</title>
<link rel="stylesheet" href="https://fonts.googleapis.com/css2?family=Playfair+Display+SC:wght@400;700&display=swap">
<style>
  :root {
    --page-bg: #ffffff;
    --panel: #ffffff;
    --ink: #2b2626;
    --ink-soft: #4a4545;
  }
  * { margin: 0; padding: 0; box-sizing: border-box; }
  html, body {
    width: 1200px;
    height: 1200px;
    overflow: hidden;
    background: var(--page-bg);
  }
  .canvas {
    position: relative;
    width: 1200px;
    height: 1200px;
  }
  .label {
    position: absolute;
    left: 50px;
    top: 210px;
    width: 1100px;
    height: 780px;
    overflow: hidden;
  }
  .label__foliage {
    position: absolute;
    inset: 0;
    width: 100%;
    height: 100%;
  }
  .label__panel {
    position: absolute;
    left: 161px;
    top: 144px;
    width: 754px;
    height: 483px;
    background: var(--panel);
    display: flex;
    flex-direction: column;
    align-items: center;
    justify-content: center;
    text-align: center;
    font-family: "Playfair Display SC", serif;
    color: var(--ink);
    line-height: 1;
  }
  .brand-name { font-size: 42px; font-weight: 700; letter-spacing: 0.5px; }
  .product-qualifier { font-size: 64px; font-weight: 400; margin-top: 14px; }
  .product-name { font-size: 100px; font-weight: 400; margin-top: 6px; color: var(--ink-soft); letter-spacing: 1px; }
  .product-type { font-size: 72px; font-weight: 700; margin-top: 4px; }
  .scent-name { font-size: 52px; font-weight: 400; margin-top: 22px; }
  .net-weight { font-size: 42px; font-weight: 400; margin-top: 12px; display: flex; align-items: center; gap: 14px; }
  .net-weight__divider { width: 2px; height: 42px; background: var(--ink); }
</style>
</head>
<body>
<main class="canvas">
  <section class="label">
    <svg class="label__foliage" viewBox="0 0 1100 780" preserveAspectRatio="none" role="img" aria-label="Tropical foliage pattern of violet, magenta, blue and teal leaves on a dark navy ground">
      <defs>
        <linearGradient id="foliageTone" x1="0" y1="0" x2="1" y2="1">
          <stop offset="0" stop-color="#7e5cc4"/>
          <stop offset="0.3" stop-color="#4a4b9a"/>
          <stop offset="0.55" stop-color="#8a4fb8"/>
          <stop offset="0.8" stop-color="#5a4aa8"/>
          <stop offset="1" stop-color="#a255b0"/>
        </linearGradient>
      </defs>
      <rect width="1100" height="780" fill="url(#foliageTone)"/>
    </svg>
    <div class="label__panel">
      <p class="brand-name">Kestrel &amp; Birch Co.</p>
      <p class="product-qualifier">Grass Fed</p>
      <h1 class="product-name">Beef Tallow</h1>
      <p class="product-type">Balm</p>
      <p class="scent-name">Peppermint</p>
      <p class="net-weight"><span>4 oz</span><span class="net-weight__divider"></span><span>114 g</span></p>
    </div>
  </section>
</main>
</body>
</html>
```